Business Card Design for Occupational Medicine Start Up Company

We need to design a professional business card. We are a healthcare company providing occupational medicine services to blue collar industries. We are professional, efficient and high quality service providers.

Target Market(s)

Blue Collar Industry: Shipbuilding, Ports, Trucking Companies; The Executives and Safety Officers for these companies

Industry/Entity Type

Healthcare

Contact Information for Business Card

Logo, Name, Title, Email, Phone

Other font styles liked:
• Please match our Brand Guide

Requirements
Must have
• Our Company Colors and Logo

```html
<!DOCTYPE html>
<html lang="en">
<head>
<meta charset="utf-8">
<title>ShiftWell Clinics – Business Card</title>
<link href="https://fonts.googleapis.com/css2?family=Montserrat:wght@400;700&family=Questrial&display=swap" rel="stylesheet">
<style>
  :root {
    --navy: #2e3588;
    --sky: #29abe2;
    --amber: #f9b552;
    --card: #ebebeb;
    --ink: #6d6e71;
    --stage: #d9d9d9;
  }
  * { box-sizing: border-box; margin: 0; padding: 0; }
  html, body { width: 1200px; height: 1107px; overflow: hidden; }
  body { background: var(--stage); position: relative; font-family: "Questrial", sans-serif; }

  .card { position: absolute; left: 236px; width: 804px; height: 460px; background: var(--card); overflow: hidden; }
  .card--front { top: 69px; }
  .card--back { top: 579px; }

  .stripes { position: absolute; left: 0; right: 0; bottom: 0; height: 42px; }
  .stripe { position: absolute; left: 0; right: 0; }
  .stripe--amber { top: 0; height: 7px; background: var(--amber); }
  .stripe--sky { top: 13px; height: 9px; background: var(--sky); }
  .stripe--navy { top: 28px; height: 14px; background: var(--navy); }

  .brand-mark { position: absolute; left: 86px; top: 226px; display: flex; align-items: center; gap: 10px; }
  .brand-dot { width: 26px; height: 26px; border-radius: 50%; background: var(--navy); }
  .brand-name { font-family: "Montserrat", sans-serif; font-weight: 700; font-size: 28px; color: var(--navy); letter-spacing: 0.5px; }

  .divider { position: absolute; left: 400px; top: 149px; width: 2px; height: 194px; background: var(--navy); opacity: 0.7; }

  .details { position: absolute; left: 484px; top: 142px; color: var(--ink); }
  .person-name { font-family: "Montserrat", sans-serif; font-size: 24px; color: var(--navy); line-height: 1.2; }
  .person-name .surname { color: var(--amber); }
  .person-title { font-size: 16px; margin-top: 2px; }
  .contact-list { list-style: none; margin-top: 18px; }
  .contact-list li { display: flex; align-items: center; gap: 10px; font-size: 17px; height: 28px; }
  .contact-list svg { width: 13px; height: 13px; fill: var(--navy); flex: none; }
  .contact-list .accent { color: var(--amber); }
  .address { font-size: 17px; line-height: 28px; margin-top: 4px; }

  .back-brand { position: absolute; left: 0; right: 0; top: 132px; display: flex; flex-direction: column; align-items: center; gap: 26px; }
  .back-brand .brand-dot { width: 84px; height: 84px; }
  .back-brand .brand-name { font-size: 38px; letter-spacing: 1px; }
</style>
</head>
<body>
  <section class="card card--front">
    <div class="brand-mark">
      <span class="brand-dot"></span>
      <span class="brand-name">ShiftWell</span>
    </div>
    <div class="divider"></div>
    <div class="details">
      <p class="person-name">Rania <span class="surname">Idrissi</span></p>
      <p class="person-title">Directeur</p>
      <ul class="contact-list">
        <li>
          <svg viewBox="0 0 16 16" aria-hidden="true"><path d="M3.5 1l3 3-1.6 2a9 9 0 0 0 5.1 5.1l2-1.6 3 3-2 2.5C6.5 14.5 1.5 9.5 1 3z"/></svg>
          +0212 0600 482 715
        </li>
        <li>
          <svg viewBox="0 0 16 16" aria-hidden="true"><path d="M1 3h14v10H1z" /><path d="M1 3l7 6 7-6" fill="none" stroke="#ebebeb" stroke-width="1.4"/></svg>
          r.idrissi@shiftwell.ma
        </li>
        <li>
          <svg viewBox="0 0 16 16" aria-hidden="true"><circle cx="8" cy="8" r="7"/><path d="M1 8h14M8 1c3 3 3 11 0 14M8 1c-3 3-3 11 0 14" fill="none" stroke="#ebebeb" stroke-width="1.2"/></svg>
          <span>www.<span class="accent">shiftwellcare</span>.ma</span>
        </li>
      </ul>
      <p class="address">PO BOX 10457 Parkside<br>Calgary, AB T2P-4K</p>
    </div>
    <div class="stripes">
      <div class="stripe stripe--amber"></div>
      <div class="stripe stripe--sky"></div>
      <div class="stripe stripe--navy"></div>
    </div>
  </section>

  <section class="card card--back">
    <div class="back-brand">
      <span class="brand-dot"></span>
      <span class="brand-name">SHIFTWELL CLINICS</span>
    </div>
    <div class="stripes">
      <div class="stripe stripe--amber"></div>
      <div class="stripe stripe--sky"></div>
      <div class="stripe stripe--navy"></div>
    </div>
  </section>
</body>
</html>
```